Bubble map/flip book

I need someone to create a bubble map with explanations using the attached. This will be used to create a color coded flip book/manual. I need you to clean this up.

Mirandalowsky@plinkmail.com

```html
<!DOCTYPE html>
<html lang="en">
<head>
<meta charset="utf-8">
<title>Claim Has Denied – Denial Reasons Bubble Map</title>
<link rel="stylesheet" href="https://fonts.googleapis.com/css2?family=Montserrat:wght@700&family=Staatliches&display=swap">
<style>
  :root {
    --paper: #ffffff;
    --core: #0656a4;
    --connector: #1d5fa8;
    --auth: #a98a0a;
    --timely: #e57a0a;
    --info: #0b12e6;
    --global: #5710c6;
    --wow: #454341;
    --duplicate: #0e5a0a;
    --coding: #f00a0a;
    --ink: #ffffff;
    --placeholder: rgba(255,255,255,0.28);
  }
  html, body {
    margin: 0;
    padding: 0;
    width: 1200px;
    height: 848px;
    overflow: hidden;
    background: var(--paper);
  }
  .bubble-map {
    display: block;
    width: 1200px;
    height: 848px;
  }
  .connector { stroke: var(--connector); stroke-width: 5; }
  .core { fill: var(--core); }
  .stamp-frame { fill: none; stroke: var(--ink); }
  .stamp-text {
    font-family: "Staatliches", "Impact", sans-serif;
    fill: var(--ink);
  }
  .bubble-label {
    font-family: "Montserrat", "Arial", sans-serif;
    font-weight: 700;
    font-size: 24px;
    fill: var(--ink);
    text-anchor: middle;
  }
  .icon-line { fill: none; stroke: var(--ink); stroke-width: 5; stroke-linecap: round; stroke-linejoin: round; }
  .icon-fill { fill: var(--ink); }
  .icon-mark { fill: currentColor; }
  .placeholder { fill: var(--placeholder); }
  .auth { fill: var(--auth); }
  .timely { fill: var(--timely); }
  .info { fill: var(--info); }
  .global { fill: var(--global); }
  .wow { fill: var(--wow); }
  .duplicate { fill: var(--duplicate); }
  .coding { fill: var(--coding); }
</style>
</head>
<body>
<svg class="bubble-map" viewBox="0 0 1500 1060" xmlns="http://www.w3.org/2000/svg" aria-label="Claim denial reasons bubble map">

  <!-- connectors -->
  <g class="connectors">
    <line class="connector" x1="545" y1="245" x2="572" y2="305"/>
    <line class="connector" x1="975" y1="262" x2="948" y2="318"/>
    <line class="connector" x1="1188" y1="480" x2="1122" y2="488"/>
    <line class="connector" x1="1115" y1="685" x2="1055" y2="648"/>
    <line class="connector" x1="770" y1="745" x2="770" y2="805"/>
    <line class="connector" x1="425" y1="728" x2="468" y2="678"/>
    <line class="connector" x1="310" y1="445" x2="362" y2="460"/>
  </g>

  <!-- central node -->
  <g class="core-node">
    <ellipse class="core" cx="738" cy="510" rx="388" ry="235"/>
    <g transform="rotate(-8 742 508)">
      <rect class="stamp-frame" x="462" y="375" width="560" height="268" rx="16" stroke-width="9"/>
      <rect class="stamp-frame" x="478" y="390" width="528" height="238" rx="10" stroke-width="4"/>
      <text class="stamp-text" x="742" y="486" font-size="118" text-anchor="middle" letter-spacing="6">CLAIM HAS</text>
      <text class="stamp-text" x="742" y="615" font-size="170" text-anchor="middle" letter-spacing="8">DENIED</text>
    </g>
  </g>

  <!-- Auth referral needed -->
  <g class="bubble bubble-auth">
    <ellipse class="auth" cx="515" cy="142" rx="140" ry="105"/>
    <rect class="placeholder" x="440" y="48" width="140" height="110" rx="14" role="img" aria-label="Referral icon: two people with a return arrow"/>
    <text class="bubble-label" x="515" y="212">AUTH REFERAL</text>
    <text class="bubble-label" x="515" y="237">NEEDED</text>
  </g>

  <!-- Past timely filing -->
  <g class="bubble bubble-timely">
    <ellipse class="timely" cx="983" cy="160" rx="140" ry="105"/>
    <path class="icon-line" d="M900 100 L950 88 L972 178 L920 192 Z"/>
    <path class="icon-line" d="M912 118 L952 108 M916 134 L956 124 M920 150 L960 140 M924 166 L964 156"/>
    <circle class="icon-line" cx="1022" cy="148" r="38" fill="var(--timely)"/>
    <path class="icon-line" d="M1022 122 V148 L1004 166"/>
    <text class="bubble-label" x="983" y="232">PAST TIMELY</text>
    <text class="bubble-label" x="983" y="257">FILING</text>
  </g>

  <!-- Additional information requested -->
  <g class="bubble bubble-info">
    <ellipse class="info" cx="1322" cy="445" rx="140" ry="105"/>
    <circle class="icon-line" cx="1332" cy="402" r="46"/>
    <text x="1332" y="424" font-family="Georgia, serif" font-style="italic" font-weight="700" font-size="58" fill="#fff" text-anchor="middle">i</text>
    <circle class="icon-fill" cx="1270" cy="424" r="24"/>
    <path d="M1270 410 V438 M1256 424 H1284" stroke="var(--info)" stroke-width="6"/>
    <text class="bubble-label" x="1322" y="482">ADDITIONAL</text>
    <text class="bubble-label" x="1322" y="506">INFORMATION</text>
    <text class="bubble-label" x="1322" y="530">REQUESTED</text>
  </g>

  <!-- Global inclusive -->
  <g class="bubble bubble-global">
    <ellipse class="global" cx="1205" cy="762" rx="138" ry="105"/>
    <circle class="icon-line" cx="1212" cy="738" r="58"/>
    <ellipse class="icon-line" cx="1212" cy="738" rx="26" ry="58"/>
    <path class="icon-line" d="M1154 738 H1270 M1162 710 H1262 M1162 766 H1262 M1212 680 V796"/>
    <rect class="icon-fill" x="1112" y="722" width="110" height="30"/>
    <path d="M1122 737 H1210 M1196 726 L1210 737 L1196 748" stroke="var(--global)" stroke-width="4" fill="none"/>
    <text class="bubble-label" x="1212" y="828">GLOBAL</text>
    <text class="bubble-label" x="1212" y="852">INCLUSIVE</text>
  </g>

  <!-- WOW coverage charge -->
  <g class="bubble bubble-wow">
    <ellipse class="wow" cx="773" cy="902" rx="138" ry="105"/>
    <rect class="placeholder" x="680" y="842" width="190" height="86" rx="14" role="img" aria-label="Dollar coin with a burst reading wow"/>
    <text class="bubble-label" x="773" y="964">WOW COVERAGE</text>
    <text class="bubble-label" x="773" y="989">CHARGE</text>
  </g>

  <!-- Duplicate -->
  <g class="bubble bubble-duplicate">
    <ellipse class="duplicate" cx="338" cy="810" rx="140" ry="105"/>
    <path class="icon-line" d="M270 740 L330 728 L348 840 L290 852 Z" fill="var(--duplicate)"/>
    <path class="icon-line" d="M314 742 H380 L402 764 V856 H314 Z" fill="var(--duplicate)"/>
    <path class="icon-line" d="M328 770 H388 M328 786 H388 M328 802 H388 M328 818 H388 M328 834 H388" stroke-width="3"/>
    <text class="bubble-label" x="342" y="890">DUPLICATE</text>
  </g>

  <!-- Coding / billing issues -->
  <g class="bubble bubble-coding">
    <ellipse class="coding" cx="173" cy="420" rx="140" ry="105"/>
    <text x="116" y="398" font-family="Montserrat, Arial, sans-serif" font-weight="700" font-size="36" fill="#fff" text-anchor="middle">&lt;/&gt;</text>
    <path class="icon-line" d="M178 340 L232 346 L256 378 L246 458 L160 448 Z"/>
    <path class="icon-line" d="M190 372 H236 M186 392 H232 M184 412 H214 M182 432 H212" stroke-width="4"/>
    <text x="226" y="446" font-family="Montserrat, Arial, sans-serif" font-weight="700" font-size="22" fill="#fff" text-anchor="middle">$</text>
    <text class="bubble-label" x="173" y="488">CODING / BILLING</text>
    <text class="bubble-label" x="173" y="513">ISSUES</text>
  </g>
</svg>
</body>
</html>
```